Larchmont Holdings Needs New Stationery Design

We need new clean and white stationery for our property management company based in Winnipeg, Manitoba, Canada. We manage condominium and commercial properties. Additionally, we do real estate development and commercial leasing.

We'll require the following:
- Business cards
- Letterhead*
- Envelope (we mainly use #10, single window envelope)
- Fax Cover Sheet
- *Electronic version of the letterhead that works in Google Docs (.jpg for top header)

Industry/Entity Type

Property Management

```html
<!DOCTYPE html>
<html lang="en">
<head>
<meta charset="utf-8">
<title>Larchmont Holdings Stationery</title>
<link href="https://fonts.googleapis.com/css2?family=Questrial&family=Arimo:wght@400;700&display=swap" rel="stylesheet">
<style>
  :root {
    --navy: #2b3d6e;
    --cyan: #1aa3d8;
    --ink: #1f1f1f;
    --paper: #ffffff;
    --backdrop: #e4e5e7;
    --rule: #d5d7da;
  }
  * { margin: 0; padding: 0; box-sizing: border-box; }
  html, body { width: 1200px; height: 1000px; overflow: hidden; }
  body {
    background: var(--backdrop);
    font-family: "Questrial", "Century Gothic", sans-serif;
    color: var(--ink);
    position: relative;
  }
  .sheet {
    position: absolute;
    background: var(--paper);
    box-shadow: 0 2px 6px rgba(0,0,0,.18);
    overflow: hidden;
  }

  /* wordmark */
  .wordmark {
    position: absolute;
    display: flex;
    align-items: center;
    gap: 6px;
    color: var(--navy);
    font-family: "Questrial", sans-serif;
    line-height: 1;
    white-space: nowrap;
  }
  .wordmark .mark {
    background: var(--cyan);
    flex: none;
  }
  .wordmark.on-navy { color: var(--paper); }

  /* contact block */
  .contact {
    position: absolute;
    padding-left: 10px;
    font-size: 9px;
    line-height: 1.45;
  }
  .contact::before {
    content: "";
    position: absolute;
    left: 0; top: 0; bottom: 0;
    width: 5px;
    background: var(--cyan);
  }
  .contact .row { display: flex; }
  .contact .label {
    width: 46px;
    text-align: right;
    padding-right: 3px;
    color: var(--ink);
  }
  .contact .value { color: var(--cyan); }
  .contact .gap { margin-left: 6px; }

  /* letterhead */
  .letterhead { left: 57px; top: 44px; width: 518px; height: 668px; }
  .letterhead .wordmark { left: 38px; top: 42px; font-size: 17px; }
  .letterhead .wordmark .mark { width: 9px; height: 9px; }
  .letterhead .date {
    position: absolute; right: 38px; top: 58px;
    font-size: 11px; color: var(--cyan);
  }
  .letterhead .salutation {
    position: absolute; left: 39px; top: 124px;
    font-family: "Arimo", sans-serif; font-size: 9px;
  }
  .letterhead .body {
    position: absolute; left: 39px; top: 145px; width: 417px;
    font-family: "Arimo", sans-serif; font-size: 8px; line-height: 1.48;
    color: #333;
  }
  .letterhead .body p { margin-bottom: 9px; }
  .letterhead .body p:first-child { text-indent: 92px; padding-left: 0; margin-left: 0; }
  .letterhead .body p:first-child { padding-left: 0; }
  .letterhead .contact { left: 0; top: 592px; font-size: 8px; }
  .letterhead .contact .label { width: 46px; }

  /* business card back */
  .card-back { left: 651px; top: 20px; width: 382px; height: 209px; background: var(--navy); }
  .card-back .wordmark { left: 118px; top: 96px; font-size: 24px; }
  .card-back .wordmark .mark { width: 12px; height: 12px; }
  .card-back .url {
    position: absolute; left: 127px; top: 195px;
    font-size: 9px; color: #cfd6e6; transform: translateY(-50%);
  }

  /* business card front */
  .card-front { left: 651px; top: 240px; width: 382px; height: 213px; }
  .card-front .wordmark { left: 13px; top: 24px; font-size: 17px; }
  .card-front .wordmark .mark { width: 9px; height: 9px; }
  .card-front .person {
    position: absolute; right: 22px; top: 44px; text-align: left;
    padding-right: 0;
  }
  .card-front .person .name { font-size: 19px; color: var(--cyan); line-height: 1.1; }
  .card-front .person .title {
    font-family: "Arimo", sans-serif; font-size: 11px; color: var(--ink);
  }
  .card-front .accent-right {
    position: absolute; right: 0; top: 42px; width: 7px; height: 50px; background: var(--cyan);
  }
  .card-front .contact { left: 0; top: 128px; }
  .card-front .contact .label { width: 50px; }

  /* envelope back */
  .envelope-back { left: 607px; top: 469px; width: 577px; height: 248px; }
  .envelope-back svg { position: absolute; left: 0; top: 0; }
  .envelope-back .url {
    position: absolute; right: 80px; bottom: 6px;
    font-size: 11px; color: var(--cyan);
  }

  /* envelope front */
  .envelope-front { left: 607px; top: 733px; width: 577px; height: 251px; }
  .envelope-front .wordmark { left: 23px; top: 28px; font-size: 20px; }
  .envelope-front .wordmark .mark { width: 10px; height: 10px; }
  .envelope-front .window {
    position: absolute; left: 216px; top: 68px; width: 333px; height: 96px;
    left: 216px;
    border: 1.5px solid #222; border-radius: 12px;
    left: auto; right: 23px;
  }
  .envelope-front .contact { left: 0; top: 170px; font-size: 9.5px; }
  .envelope-front .contact .label { width: 48px; }
</style>
</head>
<body>

  <!-- Letterhead -->
  <section class="sheet letterhead" aria-label="Letterhead">
    <div class="wordmark"><span class="mark"></span>Larchmont Holdings</div>
    <div class="date">Date:.......................</div>
    <p class="salutation">Dear Sir / Madam,</p>
    <div class="body">
      <p style="padding-left:0;margin-left:0;text-indent:0;padding-left:92px;">Lorem ipsum dolor sit amet, consectetur adipisicing elit, sed do eiusmod tempor labore et dolore magna aliqua. Ut enim ad minim veniam, quis nostrud exercitation ullamco laboris nisi ut aliquip ex ea commodo consequa Lorem ipsum dolor sit amet, consectetur adipisicing elit, sed do eiusmod tempor incididunt ut labore et dolore magna aliqua. Ut enim ad minim veniam, quis.</p>
      <p>Lorem ipsum dolor sit amet, consectetur adipisicing elit, sed do eiusmod tempor labore et dolore magna aliqua. Ut enim ad minim veniam, quis nostrud exercitation ullamco lab oris nisi ut aliquip ex ea commodo consequa Lorem ipsum dolor sit amet, consectetur adipisicing elit, sed do eiusmod tempor incididunt ut labore et dolore magna aliqua. Ut enim ad minim veniam, quis.</p>
      <p>Lorem ipsum dolor sit amet, consectetur adipisicing elit, sed do eiusmod tempor labore et dolore magna aliqua. Ut enim ad minim veniam, quis nostrud exercitation ullamco lab oris nisi ut aliquip ex ea commodo consequa Lorem ipsum dolor sit amet, consectetur adipisicing elit, sed do eiusmod tempor incididunt ut labore et dolore magna aliqua. Ut enim ad minim veniam, quis.</p>
    </div>
    <div class="contact">
      <div class="row"><span class="label">address:</span><span class="value">412 Elm Crescent</span></div>
      <div class="row"><span class="label"></span><span class="value gap">Winnipeg, MB R2K 4T1</span></div>
      <div class="row"><span class="label">phone:</span><span class="value">(204) 555-0143</span>&nbsp;<span class="label" style="width:auto">fax:</span><span class="value">(204) 555-0144</span></div>
      <div class="row"><span class="label">email:</span><span class="value">info@larchmontholdings.ca</span></div>
      <div class="row"><span class="label">website:</span><span class="value">www.larchmontholdings.ca</span></div>
    </div>
  </section>

  <!-- Business card, back -->
  <section class="sheet card-back" aria-label="Business card back">
    <div class="wordmark on-navy"><span class="mark"></span>Larchmont Holdings</div>
    <div class="url">www.larchmontholdings.ca</div>
  </section>

  <!-- Business card, front -->
  <section class="sheet card-front" aria-label="Business card front">
    <div class="wordmark"><span class="mark"></span>Larchmont Holdings</div>
    <div class="person">
      <div class="name">Martin Keller</div>
      <div class="title">President &amp; CEO</div>
    </div>
    <div class="accent-right"></div>
    <div class="contact">
      <div class="row"><span class="label">address:</span><span class="value">412 Elm Crescent</span></div>
      <div class="row"><span class="label"></span><span class="value gap">Winnipeg, MB R2K 4T1</span></div>
      <div class="row"><span class="label">phone:</span><span class="value">(204) 555-0143</span>&nbsp;&nbsp;<span class="label" style="width:auto">fax:</span><span class="value">(204) 555-0144</span></div>
      <div class="row"><span class="label">email:</span><span class="value">mkeller@larchmontholdings.ca</span></div>
      <div class="row"><span class="label">website:</span><span class="value">www.larchmontholdings.ca</span></div>
    </div>
  </section>

  <!-- Envelope, back -->
  <section class="sheet envelope-back" aria-label="Envelope back">
    <svg width="577" height="248" viewBox="0 0 577 248" aria-hidden="true">
      <path d="M0 0 H577 V18 C560 40 520 48 440 62 C380 72 320 80 288 88 C256 80 196 72 136 62 C56 48 16 40 0 18 Z" fill="var(--navy)"/>
    </svg>
    <div class="url">www.larchmontholdings.ca</div>
  </section>

  <!-- Envelope, front (#10 single window) -->
  <section class="sheet envelope-front" aria-label="Envelope front">
    <div class="wordmark"><span class="mark"></span>Larchmont Holdings</div>
    <div class="window"></div>
    <div class="contact">
      <div class="row"><span class="label">address:</span><span class="value">412 Elm Crescent</span></div>
      <div class="row"><span class="label"></span><span class="value gap">Winnipeg, MB R2K 4T1</span></div>
      <div class="row"><span class="label">phone:</span><span class="value">(204) 555-0143</span>&nbsp;&nbsp;<span class="label" style="width:auto">fax:</span><span class="value">(204) 555-0144</span></div>
      <div class="row"><span class="label">email:</span><span class="value">info@larchmontholdings.ca</span></div>
      <div class="row"><span class="label">website:</span><span class="value">www.larchmontholdings.ca</span></div>
    </div>
  </section>

</body>
</html>
```